Business Card Design

Retail Do It Yourself Studio/Store
I sell Lena Marsh Clay Paint and supplies to repurpose furniture. Classes are held to teach basic chalk paint techniques. Lena Marsh Quick Coat Paint does not require sanding or primer. It is not only perfect for furniture but Kitchen and Bathroom cabinets. Other classes include painting with laquer,painting with milk paint, antiquing mirrors, using zinc on stainless steel. Painting on fabric, upholstery, repurposing garage sale finds. Taking your $5 dollar item and turning it into a one of kind interior design masterpiece. Studio time is also sold. Patrons may come for a one time visit and use our paint and supplies to repurpose their furniture or they may want a membership to come anytime they want to use our supplies to work on their pieces. I will also consign repurposed pieces in the store, at local antique markets and online.

Industry/Entity Type

Painting

Contact Information for Business Card

Dora Pell
218 Wexley Blvd. Suite 407
Marlow Bay, Florida 32990
321-555-0264
https://www.example-social.test/velvetoakworkshop

```html
<!DOCTYPE html>
<html lang="en">
<head>
<meta charset="utf-8">
<title>Velvet Oak Workshop – Business Card</title>
<link rel="stylesheet" href="https://fonts.googleapis.com/css2?family=Cormorant+Garamond:wght@500;600&family=Source+Sans+3:wght@400;600&display=swap">
<style>
  :root {
    --page-bg: #e9e6e1;
    --card-white: #fbfbfa;
    --card-dark: #2b2b2c;
    --card-dark-2: #4a4a4b;
    --ink: #3a3a3a;
    --ink-soft: #6b6b6b;
    --text-light: #f2f2f2;
    --shadow: rgba(0,0,0,0.18);
  }
  * { margin: 0; padding: 0; box-sizing: border-box; }
  html, body { width: 1200px; height: 1023px; overflow: hidden; }
  body {
    background: var(--page-bg);
    font-family: "Source Sans 3", Arial, sans-serif;
    position: relative;
  }
  .card {
    position: absolute;
    left: 200px;
    width: 800px;
    height: 457px;
    overflow: hidden;
    box-shadow: 0 6px 22px var(--shadow);
  }
  .card--front { top: 36px; display: flex; background: var(--card-white); }
  .card--back  { top: 530px; }

  /* Front */
  .brand-panel {
    width: 56%;
    display: flex;
    flex-direction: column;
    align-items: center;
    justify-content: center;
    gap: 22px;
    background: linear-gradient(180deg, #ffffff, #f1f1f0);
  }
  .brand-name {
    font-family: "Cormorant Garamond", Georgia, serif;
    font-weight: 600;
    font-size: 40px;
    letter-spacing: 3px;
    color: var(--ink);
    text-transform: uppercase;
    text-align: center;
    line-height: 1.15;
  }
  .brand-tagline {
    font-family: "Cormorant Garamond", Georgia, serif;
    font-weight: 500;
    font-size: 21px;
    letter-spacing: 4px;
    color: var(--ink-soft);
    white-space: nowrap;
  }
  .contact-panel {
    width: 44%;
    position: relative;
  }
  .contact-photo {
    position: absolute; inset: 0;
    background: linear-gradient(135deg, var(--card-dark) 0%, var(--card-dark-2) 55%, #343536 100%);
  }
  .contact-info {
    position: absolute;
    left: 44px; top: 70px;
    color: var(--text-light);
    font-size: 21px;
    line-height: 1.45;
  }
  .contact-name {
    font-family: "Cormorant Garamond", Georgia, serif;
    font-weight: 600;
    font-size: 32px;
    letter-spacing: 1px;
    text-transform: uppercase;
    margin-bottom: 10px;
  }
  .contact-line { display: flex; align-items: center; gap: 10px; }
  .contact-icon { width: 17px; height: 17px; flex: none; }
  .contact-address { margin-top: 10px; }

  /* Back */
  .collage { position: absolute; inset: 0; background: #ffffff; }
  .photo { position: absolute; }
  .photo--table-art {
    left: 0; top: 0; width: 300px; height: 224px;
    background: linear-gradient(135deg, #c9a23c 0%, #b8463a 40%, #3f7fb0 75%, #d8c36a 100%);
  }
  .photo--chair {
    left: 0; top: 233px; width: 300px; height: 224px;
    background: linear-gradient(160deg, #d9d8d4 0%, #8b8478 45%, #3d5b9a 70%, #e8e8e6 100%);
  }
  .photo--dining {
    left: 309px; top: 0; width: 491px; height: 457px;
    background: linear-gradient(140deg, #e6e3dc 0%, #cfcbc1 40%, #d8dc8a 62%, #bfc2a4 78%, #6fb3ae 100%);
  }
  .back-brand {
    position: absolute;
    left: 389px; top: 175px; width: 330px;
    display: flex; flex-direction: column; align-items: center; gap: 14px;
  }
  .back-brand .brand-name { font-size: 30px; }
  .back-brand .brand-tagline { font-size: 16px; color: var(--ink); }
</style>
</head>
<body>

<section class="card card--front">
  <div class="brand-panel">
    <p class="brand-name">Velvet Oak<br>Workshop</p>
    <p class="brand-tagline">Old Pieces - New Stories</p>
  </div>
  <div class="contact-panel">
    <div class="contact-photo" role="img" aria-label="Dark-toned photo of a painted white chair with a blue and white patterned cushion"></div>
    <div class="contact-info">
      <p class="contact-name">Dora Pell</p>
      <p class="contact-line">
        <svg class="contact-icon" viewBox="0 0 20 20" aria-hidden="true">
          <rect width="20" height="20" rx="3" fill="#f2f2f2"/>
          <path d="M6 4c1 0 1.6 2.4 1.6 3 0 .6-1 1-1 1.4 0 1 2.8 4 4 4 .4 0 .8-1 1.4-1 .6 0 3 .6 3 1.6 0 1.2-1.6 2-2.6 2C8.6 15 5 11.4 5 7c0-1 .8-3 1-3z" fill="#2b2b2c"/>
        </svg>
        321-555-0264
      </p>
      <p class="contact-line">
        <svg class="contact-icon" viewBox="0 0 20 20" aria-hidden="true">
          <rect width="20" height="20" rx="3" fill="#f2f2f2"/>
        </svg>
        /velvetoakworkshop
      </p>
      <p class="contact-address">218 Wexley Blvd.<br>Suite 407 Marlow Bay,<br>Florida 32990</p>
    </div>
  </div>
</section>

<section class="card card--back">
  <div class="collage">
    <div class="photo photo--table-art" role="img" aria-label="Photo of a repurposed table with a colourful painted top and yellow legs"></div>
    <div class="photo photo--chair" role="img" aria-label="Photo of a white painted chair with a blue and white patterned cushion"></div>
    <div class="photo photo--dining" role="img" aria-label="Photo of a white painted dining table with lime green upholstered chairs"></div>
    <div class="back-brand">
      <p class="brand-name">Velvet Oak<br>Workshop</p>
      <p class="brand-tagline">Old Pieces - New Stories</p>
    </div>
  </div>
</section>

</body>
</html>
```